Your complete Gardening and lawn maintenance, Horticultural care. (to be on card)
We are looking at using a logo of a tree, with a recycling emblem circling the tree. The colors of choice, are burnt oranges and olive greens. Presented; simple to the eye, yet catchy to the clients in a eco-friendly way. We have uploaded a design for you to look at just to give a rough idea, you can use that or create your own ideas or play around with a mixture.

Target Market(s)

Home owners, businesses, real estates.

Industry/Entity Type

Recycling

Contact Information for Business Card

Name: Derek Ostrowe
Phone: 0421583906
Email: bramblewoodyards@mailnest.net

Logo Text

Bramble-Wood Yards

Logo styles of interest
Emblem Logo
Pictorial/Combination Logo
Abstract Logo
Requirements
Must have
• Business name: Bramble-Wood Yards
and slogan : Your complete Gardening and lawn maintenance, Horticultural care

```html
<!DOCTYPE html>
<html lang="en">
<head>
<meta charset="utf-8">
<title>Bramble-Wood Yards – Business Card</title>
<link rel="stylesheet" href="https://fonts.googleapis.com/css2?family=Arimo:wght@700&display=swap">
<style>
  :root {
    --orange-deep: #f0901a;
    --orange-mid: #f39c22;
    --orange-light: #f8b232;
    --ink: #1e1e1c;
    --leaf-dark: #1f8a3c;
    --leaf-light: #7cc242;
  }
  html, body {
    margin: 0;
    padding: 0;
    width: 741px;
    height: 1200px;
    overflow: hidden;
  }
  .card {
    position: relative;
    width: 741px;
    height: 1200px;
    overflow: hidden;
    background:
      linear-gradient(172deg, rgba(255,255,255,0.06) 0%, rgba(255,255,255,0) 30%, rgba(255,255,255,0.07) 55%, rgba(0,0,0,0) 75%),
      linear-gradient(180deg, var(--orange-deep) 0%, var(--orange-mid) 45%, var(--orange-light) 100%);
    font-family: "Arimo", Arial, Helvetica, sans-serif;
    font-weight: 700;
    color: var(--ink);
  }
  .brand-circle {
    position: absolute;
    left: 220px;
    top: 112px;
    width: 300px;
    height: 300px;
    border: 18px solid var(--ink);
    border-radius: 50%;
    box-sizing: border-box;
    display: flex;
    align-items: center;
    justify-content: center;
  }
  .slogan {
    width: 210px;
    margin: 0;
    text-align: center;
    font-size: 22px;
    line-height: 1.25;
  }
  .business-name,
  .phone,
  .contact-name,
  .contact-email {
    position: absolute;
    left: 0;
    width: 741px;
    margin: 0;
    text-align: center;
    line-height: 1;
    white-space: nowrap;
  }
  .business-name { top: 462px; font-size: 56px; }
  .phone { top: 524px; font-size: 108px; }
  .contact-name { top: 654px; font-size: 36px; }
  .contact-email { top: 697px; font-size: 36px; }
  .foliage {
    position: absolute;
    left: 0;
    top: 757px;
    width: 741px;
    height: 443px;
  }
</style>
</head>
<body>
  <div class="card">
    <div class="brand-circle">
      <p class="slogan">Your complete Gardening and lawn maintenance, Horticultural care</p>
    </div>

    <p class="business-name">Bramble-Wood Yards</p>
    <p class="phone">0421583906</p>
    <p class="contact-name">Derek Ostrowe</p>
    <p class="contact-email">bramblewoodyards@mailnest.net</p>

    <svg class="foliage" role="img" aria-label="Illustration of a leafy green tree branch across the bottom of the card" viewBox="0 0 741 443" preserveAspectRatio="none">
      <defs>
        <linearGradient id="foliageTone" x1="0" y1="0" x2="1" y2="1">
          <stop offset="0" stop-color="#7cc242"/>
          <stop offset="0.55" stop-color="#3fa447"/>
          <stop offset="1" stop-color="#1f8a3c"/>
        </linearGradient>
      </defs>
      <path d="M0 20 C60 0 120 10 170 30 C240 60 320 50 400 40 C480 30 540 20 600 45 C660 70 710 80 741 95 L741 443 L0 443 Z" fill="url(#foliageTone)"/>
    </svg>
  </div>
</body>
</html>
```